e-Book Cover Design Project

I need an e-book cover design for a book called The Quiet Orchard. A handbook for hearts (turned sour). It is non-fiction. It has an apple theme throughout so I would like to see designs that use a red apple (perhaps even a bite out of it), simple text and simple background. Despite the theme, the final design should still be positive.

Target Market(s)

Most likely women aged 25 and over.

Requirements
Must have
• real red apple
Nice to have
• cupids arrow
Should not have
• cartoons

```html
<!DOCTYPE html>
<html lang="en">
<head>
<meta charset="utf-8">
<title>The Quiet Orchard — e-Book Cover</title>
<link rel="stylesheet" href="https://fonts.googleapis.com/css2?family=Cinzel:wght@400;700&family=Raleway:wght@200;300&display=swap">
<style>
  :root {
    --paper: #ffffff;
    --title-red: #d9363b;
    --title-deep: #8c1016;
    --ink: #111111;
    --author-pink: #ef5a57;
    --apple-light: #e8434a;
    --apple-mid: #b3121c;
    --apple-dark: #6e0a10;
  }
  * { margin: 0; padding: 0; box-sizing: border-box; }
  html, body {
    width: 800px;
    height: 1200px;
    overflow: hidden;
    background: var(--paper);
  }
  .cover {
    position: relative;
    width: 800px;
    height: 1200px;
    background: var(--paper);
    overflow: hidden;
  }
  .title-kicker {
    position: absolute;
    left: 138px;
    top: 58px;
    font-family: "Cinzel", serif;
    font-weight: 400;
    font-size: 70px;
    line-height: 1;
    color: var(--title-deep);
  }
  .title-line {
    position: absolute;
    right: 85px;
    font-family: "Cinzel", serif;
    font-weight: 400;
    line-height: 1;
    color: var(--title-red);
    white-space: nowrap;
  }
  .title-line--first { top: 118px; font-size: 150px; }
  .title-line--second { top: 252px; font-size: 112px; }
  .subtitle {
    position: absolute;
    left: 0;
    width: 800px;
    text-align: center;
    font-family: "Cinzel", serif;
    font-weight: 700;
    color: var(--ink);
    line-height: 1;
  }
  .subtitle--main { top: 474px; font-size: 46px; }
  .subtitle--tail { top: 962px; font-size: 54px; }
  .artwork {
    position: absolute;
    left: 225px;
    top: 545px;
    width: 400px;
    height: 405px;
    border-radius: 48% 48% 46% 46% / 44% 44% 56% 56%;
    background: radial-gradient(circle at 30% 28%, var(--apple-light) 0%, var(--apple-mid) 55%, var(--apple-dark) 100%);
  }
  .author {
    position: absolute;
    left: 0;
    top: 1108px;
    width: 800px;
    text-align: center;
    font-family: "Raleway", sans-serif;
    font-weight: 200;
    font-size: 54px;
    line-height: 1;
    color: var(--author-pink);
  }
</style>
</head>
<body>
  <main class="cover">
    <h1 class="book-title">
      <span class="title-kicker">THE</span>
      <span class="title-line title-line--first">QUIET</span>
      <span class="title-line title-line--second">ORCHARD</span>
    </h1>
    <p class="subtitle subtitle--main">A Handbook for Hearts</p>
    <div class="artwork" role="img" aria-label="Photograph of a red apple with a heart-shaped piece cut from its skin, pierced by a golden cupid's arrow"></div>
    <p class="subtitle subtitle--tail">(Turned Sour)</p>
    <p class="author">Maren Whitfield</p>
  </main>
</body>
</html>
```